DOVVRANTI Label and bottle design

We have already provided attached an idea concept of a label and bottle shape example, we now require designers to take this basic concept and advance it to the final label design using your own design creativity.
Please see attached the full product brief

```html
<!DOCTYPE html>
<html lang="en">
<head>
<meta charset="utf-8">
<title>DOVVRANTI INKORA Label</title>
<link href="https://fonts.googleapis.com/css2?family=Montserrat:wght@500;600;700;800&display=swap" rel="stylesheet">
<style>
  :root {
    --stage: #4b4b4b;
    --label-black: #141414;
    --brand-yellow: #ece31c;
    --panel-white: #f4f4f4;
    --ink: #1a1a1a;
    --muted: #3a3a3a;
    --side-text: #d8d8d8;
  }
  * { margin: 0; padding: 0; box-sizing: border-box; }
  html, body { width: 1200px; height: 654px; overflow: hidden; }
  body {
    background: var(--stage);
    font-family: "Montserrat", Arial, sans-serif;
    position: relative;
  }
  .label {
    position: absolute;
    left: 60px; top: 30px;
    width: 1080px; height: 594px;
  }
  .label-shapes { position: absolute; inset: 0; }
  .abs { position: absolute; }

  .product-title {
    left: 300px; width: 480px; top: 36px;
    text-align: center; font-size: 40px; font-weight: 800;
    color: var(--ink); letter-spacing: 0.5px;
  }
  .product-subtitle {
    left: 300px; width: 480px; top: 96px;
    text-align: center; font-size: 15px; font-weight: 700;
    color: var(--ink); letter-spacing: -0.2px;
  }
  .brand-name {
    left: 300px; width: 480px; top: 178px;
    text-align: center; font-size: 44px; font-weight: 800;
    color: var(--panel-white); letter-spacing: 1px;
  }
  .brand-tagline {
    left: 300px; width: 480px; top: 244px;
    text-align: center; font-size: 13px; font-weight: 700;
    color: var(--panel-white); letter-spacing: 3px;
  }

  .info-panel {
    left: 372px; width: 336px; top: 318px;
    text-align: center; color: var(--ink);
  }
  .claim {
    font-size: 10px; font-weight: 800; padding: 6px 0;
    border-bottom: 1.5px solid var(--brand-yellow);
  }
  .claim:first-child { padding-top: 0; }
  .uses-heading {
    font-size: 15px; font-weight: 700; padding: 6px 0;
    border-bottom: 1.5px solid var(--brand-yellow);
  }
  .uses-copy {
    font-size: 9.5px; font-weight: 500; line-height: 1.4;
    color: var(--muted); padding: 10px 14px 0;
  }

  .side-panel { top: 60px; width: 250px; color: var(--side-text); }
  .side-panel.safety { left: 24px; }
  .side-panel.directions { left: 806px; }
  .side-heading {
    font-size: 17px; font-weight: 700; color: var(--brand-yellow);
    margin-bottom: 14px;
  }
  .step-title {
    font-size: 12px; font-weight: 700; color: var(--brand-yellow);
    padding-bottom: 4px; border-bottom: 1.5px solid var(--brand-yellow);
    margin-bottom: 5px;
  }
  .step-text {
    font-size: 9.5px; font-weight: 500; line-height: 1.4;
    margin-bottom: 14px;
  }
  .side-note { font-size: 9px; font-weight: 600; color: var(--brand-yellow); }

  .net-weight {
    left: 510px; width: 60px; top: 570px;
    text-align: center; font-size: 9px; font-weight: 700;
    color: var(--brand-yellow);
  }
</style>
</head>
<body>
  <div class="label">
    <svg class="label-shapes" viewBox="0 0 1080 594" width="1080" height="594" aria-hidden="true">
      <rect x="0" y="0" width="1080" height="594" fill="var(--label-black)"/>
      <rect x="0" y="0" width="1080" height="28" fill="var(--brand-yellow)"/>
      <polygon points="300,0 780,0 780,100 740,140 340,140 300,100" fill="var(--brand-yellow)"/>
      <path d="M 318 560 Q 318 330 408 300" stroke="var(--brand-yellow)" stroke-width="22" fill="none"/>
      <path d="M 762 560 Q 762 330 672 300" stroke="var(--brand-yellow)" stroke-width="22" fill="none"/>
      <path d="M 360 560 L 360 340 Q 360 290 410 290 L 670 290 Q 720 290 720 340 L 720 560 Z" fill="var(--panel-white)"/>
      <line x1="290" y1="40" x2="290" y2="545" stroke="var(--brand-yellow)" stroke-width="2"/>
      <line x1="790" y1="40" x2="790" y2="545" stroke="var(--brand-yellow)" stroke-width="2"/>
      <rect x="0" y="560" width="1080" height="34" fill="var(--brand-yellow)"/>
      <polygon points="522,577 531,562 549,562 558,577 549,592 531,592" fill="var(--label-black)"/>
    </svg>

    <div class="abs product-title">INKORA</div>
    <div class="abs product-subtitle">ADVANCED ANILOX CLEANING GEL</div>

    <div class="abs brand-name">DOVVRANTI</div>
    <div class="abs brand-tagline">PROFESSIONAL CLEANING</div>

    <div class="abs info-panel">
      <div class="claim">NON CAUSTIC | NON TOXIC</div>
      <div class="claim">NON FLAMMABLE | NON CORROSIVE</div>
      <div class="uses-heading">USES INKORA</div>
      <p class="uses-copy">INKORA is a highly concentrated, powerful cleaning gel formulated to safely remove solvent-based, water-based, and UV inks from anilox rollers. Its thickened formula clings to surfaces, allowing deep penetration into anilox cells and is safe for use on both ceramic and chrome rollers. INKORA Gel is also suitable for general pressroom cleaning of machinery, components and floors. Additionally, it can be used to remove most varnishes, coatings, and emulsion adhesives.</p>
    </div>

    <div class="abs side-panel safety">
      <div class="step-title">SAFETY</div>
      <p class="step-text">Wear gloves and eye protection during use.</p>
      <div class="step-title">HANDLING</div>
      <p class="step-text">Keep container closed when not in use.</p>
      <div class="step-title">PRECAUTION</div>
      <p class="step-text">Keep out of reach of children.</p>
    </div>

    <div class="abs side-panel directions">
      <div class="side-heading">DIRECTIONS</div>
      <div class="step-title">APPLY</div>
      <p class="step-text">Apply gel evenly to the anilox roller surface.</p>
      <div class="step-title">DWELL TIME</div>
      <p class="step-text">Allow the gel to work for two to five minutes.</p>
      <div class="step-title">AGITATE</div>
      <p class="step-text">Use a soft brush to lift ink from the cells.</p>
      <div class="step-title">RINSE THOROUGHLY</div>
      <p class="step-text">Rinse the roller with water to remove all residue.</p>
      <p class="side-note">For more information see the data sheet.</p>
    </div>

    <div class="abs net-weight">1KG</div>
  </div>
</body>
</html>
```